Redesign business cards

We have a new logo and I am not that happy with the layout of our existing card and looking for a change. Font is a bit small and the green can be hard to read. Logo may need a tidy up as the copy I have is not that hi-res too so require you to produce a hi-res version of the logo for us too. There will be three individual business cards to produce with just the names and phone numbers being different. Address will change too, but use what you see on the card for now.

Industry/Entity Type

Business

Requirements
Nice to have
• You could consider a redesign to the new logo, just not too radical. We like the blue and green hexagons as we feel that they are representative of oil industry that we are in.

```html
<!DOCTYPE html>
<html lang="en">
<head>
<meta charset="utf-8">
<title>Tellora Oil Services – Business Card</title>
<link href="https://fonts.googleapis.com/css2?family=Montserrat:wght@400;500;600;700&display=swap" rel="stylesheet">
<style>
  :root {
    --page-bg: #e8e6e2;
    --card-top: #d9eaf2;
    --card-mid: #7cc6e8;
    --card-bottom: #0f86c2;
    --brand-green: #4e8a16;
    --ink-navy: #0b2f4a;
    --ink-soft: #2a5470;
    --text-white: #ffffff;
    --rule: rgba(11, 47, 74, 0.35);
  }
  * { box-sizing: border-box; margin: 0; padding: 0; }
  html, body {
    width: 1200px;
    height: 900px;
    overflow: hidden;
    background: var(--page-bg);
    font-family: "Montserrat", sans-serif;
  }
  .card {
    position: absolute;
    left: 150px;
    top: 193px;
    width: 900px;
    height: 514px;
    background: linear-gradient(170deg, var(--card-top) 0%, var(--card-mid) 55%, var(--card-bottom) 100%);
    box-shadow: 0 10px 30px rgba(0, 0, 0, 0.18);
    color: var(--ink-navy);
  }
  .brand {
    position: absolute;
    left: 48px;
    top: 48px;
    display: flex;
    align-items: center;
    gap: 22px;
  }
  .brand-mark {
    width: 74px;
    height: 74px;
    background: var(--brand-green);
  }
  .brand-name {
    font-weight: 700;
    font-size: 52px;
    letter-spacing: 0.5px;
    color: var(--brand-green);
    line-height: 1;
  }
  .brand-web {
    position: absolute;
    left: 144px;
    top: 140px;
    width: 500px;
    border-top: 1px solid var(--rule);
    padding-top: 10px;
    text-align: right;
    font-size: 17px;
    font-weight: 500;
    color: var(--ink-soft);
  }
  .person {
    position: absolute;
    left: 48px;
    top: 196px;
  }
  .person-name {
    font-weight: 600;
    font-size: 32px;
    letter-spacing: 0.5px;
    color: var(--ink-navy);
  }
  .person-role {
    font-weight: 500;
    font-size: 20px;
    margin-top: 4px;
    color: var(--ink-soft);
  }
  .contact {
    position: absolute;
    right: 44px;
    bottom: 36px;
    list-style: none;
    text-align: right;
    font-weight: 500;
    font-size: 20px;
    color: var(--text-white);
  }
  .contact-item {
    display: flex;
    justify-content: flex-end;
    align-items: center;
    gap: 12px;
    margin-top: 12px;
    line-height: 1.35;
  }
  .contact-icon { width: 22px; height: 22px; flex: none; }
</style>
</head>
<body>
  <section class="card" aria-label="Business card">
    <div class="brand">
      <span class="brand-mark"></span>
      <span class="brand-name">Tellora Oil Services</span>
    </div>
    <div class="brand-web">www.tellora.com.au</div>

    <div class="person">
      <p class="person-name">CALLUM FERRIGAN NZCE (MECH) P&amp;P</p>
      <p class="person-role">Director</p>
    </div>

    <ul class="contact">
      <li class="contact-item">
        <span>(office) - &nbsp; +614 555 01842</span>
        <svg class="contact-icon" viewBox="0 0 20 20" aria-hidden="true"><rect x="5" y="1.5" width="10" height="17" rx="2" fill="none" stroke="#fff" stroke-width="1.6"/><circle cx="10" cy="15.5" r="1" fill="#fff"/></svg>
      </li>
      <li class="contact-item">
        <span>callum@tellora.co.nz</span>
        <svg class="contact-icon" viewBox="0 0 20 20" aria-hidden="true"><rect x="1.5" y="4.5" width="17" height="11" fill="none" stroke="#fff" stroke-width="1.6"/><path d="M1.5 4.5 L10 11 L18.5 4.5" fill="none" stroke="#fff" stroke-width="1.6"/></svg>
      </li>
      <li class="contact-item">
        <span>Tellora Oil Services 417 Harlow Street, PO Box 5119<br>Brackley Vale Queensland 4150</span>
        <svg class="contact-icon" viewBox="0 0 20 20" aria-hidden="true"><path d="M10 19 C5 13 3.5 10.5 3.5 7.5 A6.5 6.5 0 0 1 16.5 7.5 C16.5 10.5 15 13 10 19 Z" fill="#fff"/><circle cx="10" cy="7.5" r="2.3" fill="#1a90c8"/></svg>
      </li>
    </ul>
  </section>
</body>
</html>
```